pet sitting business brochure

please create a professional bold brochure for my new pet sitting business
please use my logo and collect suitable photos online to go with design of brochure
my colour theme is orange and blue
please look at my website to collect information
www.brindlepawminders.com.au

Reason: extended until tomorrow to make any changes to designs

```html
<!DOCTYPE html>
<html lang="en">
<head>
<meta charset="utf-8">
<title>Brindle Paw Minders – Trifold Brochure</title>
<link href="https://fonts.googleapis.com/css2?family=Oswald:wght@400;500;600;700&family=Roboto:wght@400;700&display=swap" rel="stylesheet">
<style>
  :root{
    --sky:#cce9f8;
    --peach:#fde8d4;
    --mint:#eaf4ef;
    --orange:#f5862e;
    --blue:#1e8ff0;
    --deep-blue:#1b7fd6;
    --steel:#4a86c8;
    --ink:#2a2a2a;
    --grey:#8a8a8a;
    --note-shadow:#b79a82;
    --pin:#d9222a;
    --white:#ffffff;
    --frame:#8a8a8a;
  }
  html,body{margin:0;padding:0;overflow:hidden;}
  body{width:1200px;height:889px;background:var(--white);position:relative;font-family:"Oswald",sans-serif;}
  .sheet{position:absolute;left:33px;top:24px;width:1138px;height:811px;border:1px solid var(--frame);box-sizing:border-box;overflow:hidden;}
  .panel{position:absolute;top:0;height:100%;}
  .panel--prices{left:0;width:378px;background:var(--sky);border-right:1px solid var(--frame);}
  .panel--back{left:378px;width:379px;background:var(--peach);border-right:1px solid var(--frame);}
  .panel--cover{left:757px;width:381px;background:var(--mint);}

  /* price list */
  .prices{position:absolute;left:0;right:0;top:62px;text-align:center;color:var(--ink);}
  .prices p{margin:0;}
  .prices__title{font-size:20px;font-weight:600;height:34px;}
  .prices__group{font-size:17px;font-weight:600;color:var(--blue);height:30px;}
  .prices__visit{font-size:16px;font-weight:500;height:27px;}
  .prices__row{font-size:14px;font-weight:500;height:26px;}
  .prices__quote{font-size:14px;font-weight:500;color:var(--orange);height:26px;}
  .prices__gap{height:28px;}

  /* contact bands */
  .band{position:absolute;left:0;right:0;top:686px;height:110px;color:var(--white);}
  .band--orange{background:var(--orange);}
  .band--blue{background:var(--blue);}
  .strip{position:absolute;left:0;right:0;top:796px;height:15px;}
  .strip--blue{background:var(--deep-blue);}
  .strip--orange{background:var(--orange);}
  .strip--steel{background:var(--steel);}
  .contact{position:absolute;left:0;right:0;top:28px;text-align:center;font-family:"Roboto",sans-serif;font-weight:700;font-size:21px;line-height:29px;}

  /* back panel */
  .photo{position:absolute;}
  .photo--parrot{left:0;top:0;width:379px;height:285px;background:linear-gradient(120deg,#f2f2f2 0%,#e9c98a 35%,#2c7fc9 60%,#d9dde3 100%);}
  .note-shadow{position:absolute;left:38px;top:340px;width:320px;height:318px;background:var(--note-shadow);transform:rotate(1.5deg);}
  .note{position:absolute;left:22px;top:328px;width:320px;height:318px;background:var(--white);box-shadow:0 1px 3px rgba(0,0,0,.25);}
  .pin{position:absolute;left:27px;top:322px;}
  .brand{position:absolute;left:0;right:0;display:flex;align-items:center;justify-content:center;gap:8px;}
  .brand__dot{width:14px;height:14px;border-radius:50%;background:var(--orange);}
  .brand__name{font-family:"Oswald",sans-serif;font-weight:600;font-size:26px;letter-spacing:1px;color:var(--blue);}
  .brand__tag{position:absolute;left:0;right:0;text-align:center;font-family:"Roboto",sans-serif;font-size:8px;color:var(--blue);}
  .note .brand{top:116px;}
  .note .brand__tag{top:158px;}
  .address{position:absolute;left:0;right:0;top:210px;text-align:center;font-family:"Roboto",sans-serif;font-weight:700;font-size:22px;color:var(--grey);}

  /* cover */
  .panel--cover .brand{top:102px;}
  .panel--cover .brand__tag{top:146px;}
  .cover-art{position:absolute;left:0;top:185px;}
  .tagline{position:absolute;left:36px;right:10px;top:6px;font-family:"Oswald",sans-serif;color:var(--white);}
  .tagline__head{font-size:22px;font-weight:600;line-height:30px;margin:0;}
  .tagline__list{font-family:"Roboto",sans-serif;font-size:15px;line-height:20px;margin:2px 0 0;}

  .label{position:absolute;top:838px;font-family:"Roboto",sans-serif;font-size:29px;color:var(--ink);text-align:center;}
</style>
</head>
<body>
<main class="sheet">
  <section class="panel panel--prices">
    <div class="prices">
      <p class="prices__title">Prices:</p>
      <p class="prices__group">Pet Sitting</p>
      <p class="prices__visit">Once Daily visit</p>
      <p class="prices__row">1 - 2 Pets: $25</p>
      <p class="prices__row">3 - 4 Pets: $30</p>
      <p class="prices__quote">More: Ask for quote</p>
      <div class="prices__gap"></div>
      <p class="prices__visit">Twice Daily Visit</p>
      <p class="prices__row">1 - 2 Pets: $40</p>
      <p class="prices__row">3 - 4 Pets: $45</p>
      <p class="prices__quote">More: Ask for quote</p>
      <div class="prices__gap"></div>
      <p class="prices__group">Dog Walking</p>
      <p class="prices__row">20 minutes - $20</p>
      <p class="prices__row">40 minutes - $35</p>
      <p class="prices__row">60 minutes - $45</p>
      <div class="prices__gap"></div>
      <p class="prices__group">Additional Services:</p>
      <p class="prices__row">Horses Rugged: $5 - $15</p>
      <p class="prices__row">Medicine Administration: $5</p>
      <p class="prices__row">Plant Watering: $3- $15</p>
    </div>
    <div class="band band--orange">
      <div class="contact">call: 0491570156<br>jo@brindlepawminders.com.au</div>
    </div>
    <div class="strip strip--blue"></div>
  </section>

  <section class="panel panel--back">
    <div class="photo photo--parrot" role="img" aria-label="Photo of a child kissing a blue and gold macaw perched on a wooden stand"></div>
    <div class="note-shadow"></div>
    <div class="note">
      <div class="brand"><span class="brand__dot"></span><span class="brand__name">BRINDLE PAW MINDERS</span></div>
      <div class="brand__tag">We'll look after your little mates</div>
      <div class="address">Address Here</div>
    </div>
    <svg class="pin" width="40" height="44" viewBox="0 0 40 44" aria-hidden="true">
      <ellipse cx="26" cy="38" rx="10" ry="4" fill="#cfcfcf"/>
      <line x1="16" y1="22" x2="24" y2="36" stroke="#9a9a9a" stroke-width="2"/>
      <circle cx="22" cy="9" r="8" fill="var(--pin)"/>
      <circle cx="14" cy="19" r="10" fill="var(--pin)"/>
      <circle cx="11" cy="16" r="3" fill="#f27a7f"/>
    </svg>
    <div class="band band--blue">
      <div class="contact">call: 0491570156<br>jo@brindlepawminders.com.au</div>
    </div>
    <div class="strip strip--orange"></div>
  </section>

  <section class="panel panel--cover">
    <div class="brand"><span class="brand__dot"></span><span class="brand__name">BRINDLE PAW MINDERS</span></div>
    <div class="brand__tag">We'll look after your little mates</div>
    <svg class="cover-art" width="381" height="501" viewBox="0 0 381 501">
      <defs>
        <linearGradient id="cover-photo-tone" x1="0" y1="0" x2="1" y2="1">
          <stop offset="0" stop-color="#9fbf6a"/>
          <stop offset="0.45" stop-color="#c98a45"/>
          <stop offset="1" stop-color="#5f9a34"/>
        </linearGradient>
      </defs>
      <path d="M0 120 A190 120 0 0 1 381 120 L381 501 L0 501 Z" fill="var(--blue)"/>
      <path d="M0 170 Q10 60 160 42 Q300 30 381 140 L381 501 L0 501 Z" fill="url(#cover-photo-tone)" role="img" aria-label="Photo of a smiling woman lying on grass cuddling a golden retriever"/>
    </svg>
    <div class="band band--orange">
      <div class="tagline">
        <p class="tagline__head">Reliable, loving and<br>dedicated care for your pet!</p>
        <p class="tagline__list">horses, livestock, cats, dogs, rodents,<br>birds, fish, and reptiles and more..</p>
      </div>
    </div>
    <div class="strip strip--steel"></div>
  </section>
</main>

<div class="label" style="left:33px;width:378px;">back left sidepage 5</div>
<div class="label" style="left:411px;width:379px;">Back Page end page 6</div>
<div class="label" style="left:790px;width:381px;">1cover page</div>
</body>
</html>
```